Wine gifting platform needs redeem/decline page

Vintaro is a wine gifting platform. Users can send wine gifts to one or many people, the recipients will then receive an email with instructions on how to redeem their wine.

This is what we need: After clicking the link in the email they will be taken to the redeem/decline page/flow where they will choose their preferred wine and enter their shipping address. I have uploaded videos of both the decline and the redeem flows.

- All existing form fields, informational text, and error messages needs to be incorporated into the new design but otherwise you have creative freedom on presentation.
- We have four gift tiers: Silver, Gold, Platinum, and Diamond. We would like the redemption page to highlight this with different colors (or something else!) that's glanceable. I have attached screenshots to highlight these.
- Our target audience is professional and corporate but we want the redemption process to feel elegant and sleek. We want it to feel like a premium experience just like the wine they'll receive.

I would prefer Sketch files over Photoshop.

Target Market(s)

Professional, corporate

Number of Pages Required

3 page

Requirements
Must have
• All fields, all 3 steps of the wizard, information, and error messages/styles in the flow videos (attached)

```html
<!DOCTYPE html>
<html lang="en">
<head>
<meta charset="utf-8">
<title>Vintaro – Redeem Your Gift</title>
<link href="https://fonts.googleapis.com/css2?family=Roboto+Condensed:wght@400;500;700&family=Open+Sans:wght@400;700&display=swap" rel="stylesheet">
<style>
:root{
  --brand:#0a45b0;
  --ink:#1b1b1b;
  --muted:#6a6a6a;
  --step-idle:#616161;
  --panel:#f5f5f5;
  --line:#d6d6d6;
  --white:#ffffff;
  --fold:#dcdcdc;
  --wine:#3a1d22;
}
*{box-sizing:border-box;margin:0;padding:0}
html,body{width:1200px;height:2896px;overflow:hidden;background:var(--white)}
body{position:relative;font-family:"Roboto Condensed",sans-serif;color:var(--ink)}
.backdrop{position:absolute;left:0;top:0;width:1200px;height:2896px}
.screen{position:absolute;left:96px;width:1009px;height:810px;background:var(--panel);border-top:3px solid var(--brand);box-shadow:0 4px 14px rgba(0,0,0,.08);
  background-image:radial-gradient(ellipse at 100% 0%,rgba(0,0,0,.05),transparent 45%),radial-gradient(ellipse at 0% 100%,rgba(0,0,0,.04),transparent 45%)}
.screen--gift{top:126px}
.screen--address{top:1044px}
.screen--confirm{top:1964px}
.wordmark{position:absolute;left:0;right:0;top:30px;text-align:center;font-weight:700;font-size:44px;color:var(--brand);letter-spacing:1px}
.steps{position:absolute;top:135px;left:0;width:100%;height:40px}
.step{position:absolute;display:flex;align-items:center;gap:16px;font-weight:500;font-size:15px;text-transform:uppercase;color:var(--ink)}
.step__num{width:38px;height:38px;border-radius:50%;background:var(--step-idle);color:var(--white);display:flex;align-items:center;justify-content:center;font-size:17px;font-weight:700}
.step--active .step__num{background:var(--brand)}
.step--active .step__label{color:var(--brand);text-decoration:underline}
.step--1{left:223px}.step--2{left:450px}.step--3{left:679px}
.btn{position:absolute;height:44px;display:flex;align-items:center;justify-content:center;font-weight:700;font-size:15px;border:1px solid var(--brand);color:var(--brand);background:var(--white);border-radius:2px}
.btn--solid{background:var(--brand);color:var(--white)}
.tier{top:223px;width:134px;height:46px}
.collection-title{position:absolute;top:314px;left:0;right:0;text-align:center;font-size:25px;font-weight:700}
.collection-copy{position:absolute;top:357px;left:222px;width:565px;text-align:center;font-size:13.5px;line-height:22px;color:var(--muted)}
.collection-pick{position:absolute;top:423px;left:0;right:0;text-align:center;font-size:14px;font-weight:500}
.collection-pick a{color:var(--brand);margin-left:14px;font-weight:700;text-decoration:underline}
.wine-card{position:absolute;background:var(--white);border:1px solid #ececec;text-align:center;font-family:"Open Sans",sans-serif;overflow:hidden}
.wine-card::after{content:"";position:absolute;top:0;right:0;border-style:solid;border-width:0 36px 36px 0;border-color:transparent var(--fold) transparent transparent}
.wine-card--row{top:480px;width:150px;height:174px}
.bottle{display:block;margin:18px auto 0;width:22px;height:90px;border-radius:8px 8px 3px 3px;background:linear-gradient(var(--wine),#1a0e10)}
.wine-card__name{font-weight:700;font-size:13px;margin-top:12px}
.wine-card__link{display:inline-block;margin-top:8px;font-size:10px;color:var(--muted);border:1px solid var(--line);padding:2px 10px}
.field{position:absolute;width:322px}
.field__label{display:block;font-weight:700;font-size:12px;margin-left:10px;margin-bottom:8px}
.field__input{height:43px;border:1px solid var(--line);background:var(--white);border-radius:2px;font-size:11.5px;color:var(--muted);padding:0 10px;display:flex;align-items:center;justify-content:space-between}
.caret{width:0;height:0;border-left:4px solid transparent;border-right:4px solid transparent;border-top:5px solid var(--step-idle)}
.check{position:absolute;display:flex;align-items:center;gap:10px;font-size:11px;color:var(--muted);white-space:nowrap}
.check__box{width:11px;height:11px;border:1px solid var(--brand);border-radius:2px;position:relative;flex:none}
.check a{color:var(--brand);text-decoration:underline}
.check .plain-link{color:var(--brand);text-decoration:none}
.ship-note{position:absolute;top:247px;left:0;right:0;text-align:center;font-size:18px;color:var(--muted)}
.ship-address{position:absolute;top:310px;left:0;right:0;text-align:center;font-size:13.5px;font-weight:700;line-height:25px}
.gift-summary{position:absolute;left:144px;top:415px;width:720px;height:250px;border:1px solid #e2e2e2}
.gift-summary__copy{position:absolute;left:32px;top:126px;width:500px;font-size:13.5px;line-height:23.5px;color:var(--muted)}
</style>
</head>
<body>
<svg class="backdrop" viewBox="0 0 1200 2896" aria-hidden="true">
  <polygon points="0,0 1200,0 0,1018" fill="var(--brand)"/>
  <polygon points="1200,1873 1200,2896 0,2896" fill="var(--brand)"/>
</svg>

<section class="screen screen--gift">
  <div class="wordmark">Vintaro</div>
  <div class="steps">
    <div class="step step--1 step--active"><span class="step__num">01</span><span class="step__label">Choose your gift</span></div>
    <div class="step step--2"><span class="step__num">02</span><span class="step__label">Enter your address</span></div>
    <div class="step step--3"><span class="step__num">03</span><span class="step__label">Confirm</span></div>
  </div>
  <div class="btn btn--solid tier" style="left:189px">Silver</div>
  <div class="btn tier" style="left:354px">Gold</div>
  <div class="btn tier" style="left:521px">Platinum</div>
  <div class="btn tier" style="left:686px">Diamond</div>
  <h2 class="collection-title">SILVER COLLECTION</h2>
  <p class="collection-copy">"Lorem ipsum dolor sit amet, consectetur adipiscing elit, sed do eiusmod tempor incididunt ut labore et dolore magna aliqua. Ut enim ad minim veniam, quis nostrud exercitation</p>
  <p class="collection-pick">Choose Your Gift From The Silver Collection <a>Red</a></p>
  <div class="wine-card wine-card--row" style="left:105px"><span class="bottle" role="img" aria-label="Bottle of Pinot Noir"></span><div class="wine-card__name">Pinot Noir</div><span class="wine-card__link">View Details</span></div>
  <div class="wine-card wine-card--row" style="left:267px"><span class="bottle" role="img" aria-label="Bottle of Zinfandel"></span><div class="wine-card__name">Zinfandel</div><span class="wine-card__link">View Details</span></div>
  <div class="wine-card wine-card--row" style="left:430px"><span class="bottle" role="img" aria-label="Bottle of Sangiovese"></span><div class="wine-card__name">Sangiovese</div><span class="wine-card__link">View Details</span></div>
  <div class="wine-card wine-card--row" style="left:592px"><span class="bottle" role="img" aria-label="Bottle of Cabernet Sauvignon"></span><div class="wine-card__name">Cabernet Sauvignon</div><span class="wine-card__link">View Details</span></div>
  <div class="wine-card wine-card--row" style="left:755px"><span class="bottle" role="img" aria-label="Bottle of Malbec"></span><div class="wine-card__name">Malbec</div><span class="wine-card__link">View Details</span></div>
  <div class="btn btn--solid" style="left:447px;top:712px;width:115px">Next</div>
</section>

<section class="screen screen--address">
  <div class="wordmark">Vintaro</div>
  <div class="steps">
    <div class="step step--1"><span class="step__num">01</span><span class="step__label">Choose your gift</span></div>
    <div class="step step--2 step--active"><span class="step__num">02</span><span class="step__label">Enter your address</span></div>
    <div class="step step--3"><span class="step__num">03</span><span class="step__label">Confirm</span></div>
  </div>
  <div class="field" style="left:177px;top:236px"><span class="field__label">First Name</span><div class="field__input">John</div></div>
  <div class="field" style="left:511px;top:236px"><span class="field__label">Last Name</span><div class="field__input">Smith</div></div>
  <div class="field" style="left:177px;top:324px"><span class="field__label">Email Address</span><div class="field__input">johnsmith@mailbox.com</div></div>
  <div class="field" style="left:511px;top:324px"><span class="field__label">Contact Number *</span><div class="field__input">1 555 010 020</div></div>
  <div class="field" style="left:177px;top:412px"><span class="field__label">Address (Apt/Floor/Suite) *</span><div class="field__input">48 Larkin Ave, 4th Floor</div></div>
  <div class="field" style="left:511px;top:412px"><span class="field__label">City *</span><div class="field__input">New York</div></div>
  <div class="field" style="left:177px;top:500px"><span class="field__label">State *</span><div class="field__input">New York<span class="caret"></span></div></div>
  <div class="field" style="left:511px;top:500px"><span class="field__label">Postal code *</span><div class="field__input">100 001</div></div>
  <div class="check" style="left:177px;top:606px"><span class="check__box"><svg width="11" height="11" viewBox="0 0 11 11" style="position:absolute;left:0;top:-2px"><path d="M2 5.5l2.5 2.5L10 1.5" fill="none" stroke="var(--brand)" stroke-width="1.5"/></svg></span><span>I want to subscribe to emails from Vintaro to learn how to quickly and easily send wine gifts.</span></div>
  <div class="check" style="left:177px;top:639px"><span class="check__box"></span><span>I confirm that i am of legal drinking age in my state.</span></div>
  <div class="check" style="left:465px;top:639px"><span class="check__box"></span><span>I agree to the <a>Privacy policy</a> and <span class="plain-link">Terms of service.</span></span></div>
  <div class="btn" style="left:378px;top:700px;width:115px">Back</div>
  <div class="btn btn--solid" style="left:515px;top:700px;width:115px">Next</div>
</section>

<section class="screen screen--confirm">
  <div class="wordmark">Vintaro</div>
  <div class="steps">
    <div class="step step--1"><span class="step__num">01</span><span class="step__label">Choose your gift</span></div>
    <div class="step step--2"><span class="step__num">02</span><span class="step__label">Enter your address</span></div>
    <div class="step step--3 step--active"><span class="step__num">03</span><span class="step__label">Confirm</span></div>
  </div>
  <p class="ship-note">Your gift will be shipped in 1-3 businessdays and you will receive a tracking # to your email.</p>
  <div class="ship-address">AA FF<br>48 Larkin Ave, New York, NY 100001<br>(646) 555-0199- hi@vt.co</div>
  <div class="gift-summary">
    <div class="btn btn--solid" style="left:32px;top:44px;width:134px;height:46px">Pinot Noir</div>
    <p class="gift-summary__copy">"But I must explain to you how all this mistaken idea of denouncing pleasure and praising pain was born and I will give you a complete account of the system, and expound the actual teachings of the great explorer of the truth, the master-builder of human happiness. No one rejects, dislikes, or avoids pleasure itself, because it is pleasure</p>
    <div class="wine-card" style="left:564px;top:54px;width:124px;height:142px"><span class="bottle" role="img" aria-label="Bottle of Pinot Noir" style="margin-top:14px;width:18px;height:72px"></span><div class="wine-card__name" style="font-size:11px;margin-top:10px">Pinot Noir</div><span class="wine-card__link" style="font-size:8px;margin-top:6px">View Details</span></div>
  </div>
  <div class="btn" style="left:378px;top:702px;width:115px">Back</div>
  <div class="btn btn--solid" style="left:515px;top:702px;width:115px">Submit</div>
</section>
</body>
</html>
```